Korvane Systems Website

Website design for our company: Korvane Systems.
The website should look fresh and IT focused. Please have a look at http://www.korvanesystems.example.au/ for our current design. We want something fresh and new, professional looking, in WordPress so we can easily make changes.

Industry/Entity Type

It Company

```html
<!DOCTYPE html>
<html lang="en">
<head>
<meta charset="utf-8">
<title>Korvane Systems</title>
<link href="https://fonts.googleapis.com/css2?family=Open+Sans:wght@600&family=Roboto:wght@300;400;500&family=Roboto+Condensed:wght@400;700&display=swap" rel="stylesheet">
<style>
:root{
  --green-dark:#0b7a3e;
  --green:#0bb04f;
  --green-light:#5dd25f;
  --green-text:#0aa64a;
  --footer-bottom:#096c36;
  --grey-text:#8a8a8a;
  --border:#d4d4d4;
  --menu-bg:#ececec;
  --arrow:#5c5c5c;
  --white:#fff;
}
*{margin:0;padding:0;box-sizing:border-box}
html,body{width:1200px;height:1177px;overflow:hidden;background:var(--white);font-family:'Roboto',sans-serif}
.page{position:relative;width:1200px;height:1177px}
.abs{position:absolute}
.header{left:0;top:0;width:1200px;height:129px;background:var(--green-dark)}
.brand{left:173px;top:24px;width:160px;height:81px;border:2px solid var(--white);border-radius:6px;background:var(--green);display:flex;align-items:center;justify-content:center;color:var(--white);font:500 17px 'Roboto',sans-serif;white-space:nowrap}
.phone{left:670px;top:22px;display:flex;align-items:center;gap:8px;color:var(--green-light);font:400 17px 'Roboto Condensed',sans-serif}
.follow{left:813px;top:21px;color:var(--white);font:600 17px 'Open Sans',sans-serif}
.social{top:19px;width:28px;height:28px;border:2px solid #0a3f22;border-radius:50%}
.nav{left:377px;top:60px;width:651px;height:45px;background:var(--white);border:2px solid #e3e3e3;display:flex;align-items:center;list-style:none}
.nav li{font:400 13px 'Roboto',sans-serif;color:#333;padding:0 13.5px;height:100%;display:flex;align-items:center;white-space:nowrap}
.nav li.active{background:var(--green);color:var(--white);padding:0 17px;margin-left:-2px}
.card{background:var(--white);border:1px solid var(--border);border-radius:4px;box-shadow:0 1px 2px rgba(0,0,0,.08)}
.hero{left:171px;top:150px;width:858px;height:386px;overflow:visible}
.photo{left:0;top:0;width:327px;height:384px;border-radius:4px 0 0 4px;background:linear-gradient(90deg,#cfd6dc 0%,#e9ecef 70%,#fff 100%)}
.welcome-icon{left:326px;top:28px;width:52px;height:44px}
.welcome-title{left:381px;top:38px;color:var(--green-text);font:700 28px 'Roboto Condensed',sans-serif}
.intro{left:333px;top:87px;width:240px;color:var(--grey-text);font:300 13.6px/18.9px 'Roboto',sans-serif}
.intro p+p{margin-top:19px}
.btn{left:334px;top:304px;width:125px;height:28px;background:var(--green);color:var(--white);font:300 14px 'Roboto',sans-serif;display:flex;align-items:center;justify-content:center;border-radius:2px}
.side-menu{left:592px;top:52px;width:266px;height:274px;background:var(--menu-bg);border-left:1px solid var(--border);border-bottom:1px solid var(--border)}
.side-item{position:absolute;left:0;width:265px;height:53px;border-bottom:1px solid #d2d2d2;display:flex;align-items:center;padding-left:62px;color:var(--green-text);font:400 19.5px 'Roboto',sans-serif;white-space:nowrap}
.side-item .ico{position:absolute;left:13px;top:10px;width:36px;height:34px;border-radius:50%}
.side-item.active{left:0;top:0;width:285px;height:56px;background:linear-gradient(180deg,#5fd052,#10ad47);color:var(--white);border:none}
.fold{left:1029px;top:258px;width:0;height:0;border-top:17px solid #0c6d33;border-right:19px solid transparent}
.strip1{left:171px;top:553px;width:858px;height:135px}
.strip2{left:171px;top:704px;width:858px;height:137px}
.arrow{width:34px;height:34px;border-radius:50%;background:var(--arrow);display:flex;align-items:center;justify-content:center}
.tile{width:139px;height:99px;background:var(--white);border:1px solid #dcdcdc;box-shadow:0 8px 8px -6px rgba(0,0,0,.25);text-align:center}
.tile .pic{width:48px;height:50px;margin:10px auto 4px;border-radius:8px}
.tile span{color:var(--green-text);font:400 16px 'Roboto Condensed',sans-serif;white-space:nowrap}
.services-title{left:223px;top:25px;color:var(--green-text);font:400 19px 'Roboto Condensed',sans-serif}
.services-text{left:223px;top:50px;width:560px;color:var(--grey-text);font:400 12px/15.5px 'Roboto',sans-serif}
.footer{left:0;top:857px;width:1200px;height:279px;background:var(--green-dark)}
.footer h3{position:absolute;top:31px;color:var(--white);font:600 17px 'Open Sans',sans-serif;white-space:nowrap}
.footer ul{position:absolute;top:63px;list-style:none;color:var(--white);font:400 12.6px/20.6px 'Roboto',sans-serif;white-space:nowrap}
.field{left:808px;width:203px;background:var(--white);color:#666;font:400 12.5px 'Roboto',sans-serif;padding:9px 13px}
.send{left:809px;top:1072px;width:74px;height:33px;background:#0c8a43;color:var(--white);font:500 13px 'Roboto',sans-serif;display:flex;align-items:center;justify-content:center}
.bottom{left:0;top:1136px;width:1200px;height:41px;background:var(--footer-bottom);border-top:2px solid #06592b;color:var(--white);font:400 12px 'Roboto',sans-serif;display:flex;align-items:center;justify-content:center}
</style>
</head>
<body>
<div class="page">
  <header class="abs header"></header>
  <div class="abs brand">Korvane Systems</div>
  <div class="abs phone">
    <svg width="16" height="16" viewBox="0 0 24 24"><path fill="#fff" d="M6.6 10.8a15.1 15.1 0 0 0 6.6 6.6l2.2-2.2a1 1 0 0 1 1-.25 11.4 11.4 0 0 0 3.6.6 1 1 0 0 1 1 1V20a1 1 0 0 1-1 1A17 17 0 0 1 3 4a1 1 0 0 1 1-1h3.5a1 1 0 0 1 1 1c0 1.25.2 2.450.6 3.6a1 1 0 0 1-.25 1z"/></svg>
    555-0100-200
  </div>
  <div class="abs follow">FOLLOW US</div>
  <div class="abs social" style="left:929px"></div>
  <div class="abs social" style="left:965px"></div>
  <div class="abs social" style="left:1001px"></div>
  <ul class="abs nav">
    <li class="active">HOME</li><li>CLIENTS</li><li>SERVICES</li><li>SUPPORTS</li><li>TESTIMONIALS</li><li>CONTACT US</li><li>ABOUT US</li>
  </ul>

  <section class="abs card hero">
    <div class="abs photo" role="img" aria-label="Photo of a smiling office worker at a computer desk"></div>
    <div class="abs welcome-icon" role="img" aria-label="Handshake icon" style="background:linear-gradient(135deg,#2a4a6a,#6f8ba6);border-radius:10px"></div>
    <h1 class="abs welcome-title">Welcome</h1>
    <div class="abs intro">
      <p>We provide a high level of consulting services using the most experienced engineers at a reasonable and fair price. We believe in using a Business Value approach to every aspect of computer consulting to provide our clients with the most cost effective solutions.</p>
      <p>We strongly believe that we are in business with our clients.</p>
    </div>
    <div class="abs btn">Learn More</div>
    <nav class="abs side-menu">
      <div class="side-item active"><i class="ico" role="img" aria-label="Handshake icon" style="background:#2b4d6b"></i>Welcome</div>
      <div class="side-item" style="top:56px"><i class="ico" role="img" aria-label="Globe icon" style="background:radial-gradient(#9fd5f5,#2a7bc0)"></i>Website Development</div>
      <div class="side-item" style="top:110px"><i class="ico" role="img" aria-label="Gear icon" style="background:radial-gradient(#dfe7ef,#4a6f9a)"></i>Business</div>
      <div class="side-item" style="top:163px"><i class="ico" role="img" aria-label="Design compass icon" style="background:radial-gradient(#ffd46a,#2a6fb5)"></i>Web Design</div>
      <div class="side-item" style="top:216px;border-bottom:none"><i class="ico" role="img" aria-label="Repair tools icon" style="background:linear-gradient(135deg,#c9c9c9,#c0262c)"></i>Computer Repair</div>
    </nav>
  </section>
  <div class="abs fold"></div>

  <section class="abs card strip1">
    <div class="abs arrow" style="left:15px;top:50px"><svg width="10" height="10"><path d="M7 1 2 5l5 4z" fill="#fff"/></svg></div>
    <div class="abs tile" style="left:62px;top:17px"><div class="pic" role="img" aria-label="Web design icon" style="background:radial-gradient(#ffd46a,#2a6fb5)"></div><span>Web Design</span></div>
    <div class="abs tile" style="left:210px;top:17px"><div class="pic" role="img" aria-label="Globe icon" style="background:radial-gradient(#cdeaff,#3a8fd0)"></div><span>Web Development</span></div>
    <div class="abs tile" style="left:358px;top:17px"><div class="pic" role="img" aria-label="Monitor with chart icon" style="background:linear-gradient(#555,#bbb)"></div><span>Web Increase</span></div>
    <div class="abs tile" style="left:506px;top:17px"><div class="pic" role="img" aria-label="Search optimisation icon" style="background:linear-gradient(#e0e0e0,#999)"></div><span>Web Seo</span></div>
    <div class="abs tile" style="left:654px;top:17px"><div class="pic" role="img" aria-label="Mobile app icon" style="background:linear-gradient(#b7e44a,#5aa51c)"></div><span>Mobile Apps</span></div>
    <div class="abs arrow" style="left:809px;top:50px"><svg width="10" height="10"><path d="M3 1l5 4-5 4z" fill="#fff"/></svg></div>
  </section>

  <section class="abs card strip2">
    <div class="abs arrow" style="left:15px;top:51px"><svg width="10" height="10"><path d="M7 1 2 5l5 4z" fill="#fff"/></svg></div>
    <div class="abs tile" style="left:62px;top:17px"><div class="pic" role="img" aria-label="Laptop with repair tools icon" style="width:66px;background:linear-gradient(135deg,#2f5fa8,#c0262c)"></div><span>Services</span></div>
    <h2 class="abs services-title">Services</h2>
    <p class="abs services-text">We specialise in building, installing and managing customised servers for businesses of all sizes. Servers can be managed at your premises or ours.Data is stored at a central point on the server, this allows the business to control the data and set certain access restriction policies. The firewall on the server also adds security to protect your data from unauthorised access.</p>
    <div class="abs arrow" style="left:809px;top:51px"><svg width="10" height="10"><path d="M3 1l5 4-5 4z" fill="#fff"/></svg></div>
  </section>

  <footer class="abs footer">
    <h3 style="left:187px">LOCATION</h3>
    <ul style="left:188px"><li>27 Harlow Street</li><li>Brenton Park</li><li>5099 Australia</li><li>Phone:0855501234</li><li>Fax:085550 4400</li><li>Mobile:0855501234</li><li>E-mail Us: hello@korvanesystems.example</li></ul>
    <h3 style="left:408px">COMPUTER REPAIR</h3>
    <ul style="left:409px"><li>About Computer Repair</li><li>Drop-Off Computer Repair</li><li>In-Home Computer Support</li><li>Virus Removal</li><li>Desktop Support</li></ul>
    <h3 style="left:600px">WEB DESIGN</h3>
    <ul style="left:601px"><li>About Web Design</li><li>Design Portfolio</li><li>Free Web Design Consultation</li><li>The Four Elements of a Website</li><li>Web Design Pricing</li></ul>
    <h3 style="left:808px">CONTACT US</h3>
  </footer>
  <div class="abs field" style="top:925px;height:31px">Name</div>
  <div class="abs field" style="top:964px;height:31px">E-mail</div>
  <div class="abs field" style="top:1004px;height:60px">Message</div>
  <div class="abs send">Send</div>
  <div class="abs bottom">© 2014 Korvane Systems&nbsp; All Rights Reserved. Designed &amp; Developed by Pixelfern Studio</div>
</div>
</body>
</html>
```